LARGE BANNER/SIGN DESIGN - RECRUITMENT/LABOUR HIRE COMPANY

We are a Labour Hire/Recruitment company from Australia. We will need to design some signs to be displayed on all of our building sites that we are involved in. We will be printing multiple signs (up to 50) to display all over Sydney.•

• Logo nice and big, taking up majority of the sign.
• “Linking Job Seekers with Employers” – maybe under the logo or to the side of it? Please see attached cover photo.
• I want a nice simple design that incorporates some graphic like the one attached (Maroon Boxes - you do not have to use these exact graphics, but something similar).
• We want to include “www.brightpathstaffing.com.au” and “1300 482 917” somewhere on the sign.
• Maintain the colour scheme of logo throughout the sign.
• If you would like to submit your own idea, go right ahead. As long as the logo is displayed, our website and the number.

The artwork needs to be 4000mm (W) x 2500mm (H), 150dpi and saved in PDF format. Creating this artwork in Adobe Illustrator is ideal.

I have included the logo in a PDF format. This will be printed on vinyl 450gsm material. It will be better if the background is white due to the colours of the logo but we can work with anything.

Submit your creative ideas. They do not have to have any specific graphics except for the logo. The logo needs to be exactly as provided. We will also need to display the website (www.brightpathstaffing.com.au) and our number (1300 482 917) on the sign.

Target Market(s)

Construction, builders, developers, general construction industry

Industry/Entity Type

Construction

Font styles to use
Sans Serif

Colors
ec1f27
474747

Requirements
Must have
• - Logo (as provided)
• - Website (www.brightpathstaffing.com.au)
• - Phone (1300 482 917)
• - This MUST be created in Adobe Illustrator and MUST be saved in PDF with resolution 4000mm (W) x 2500mm (H) with 150 DPI. A copy of the artwork in Illustrator MUST be provided on picking winner.
Nice to have
• Creative new ideas including the logo, website and phone. Anything at all! As long as colours are followed.

```html
<!DOCTYPE html>
<html lang="en">
<head>
<meta charset="utf-8">
<title>Bright Path Staffing – Site Sign</title>
<link rel="stylesheet" href="https://fonts.googleapis.com/css2?family=Nunito:wght@600;700;800&display=swap">
<style>
  :root {
    --page: #ffffff;
    --maroon: #7d1418;
    --deep-red: #8e0a0e;
    --brand-red: #ec1f27;
    --charcoal: #474747;
    --grey-text: #6b6b6b;
    --white: #ffffff;
  }
  * { margin: 0; padding: 0; box-sizing: border-box; }
  html, body {
    width: 1200px; height: 1051px; overflow: hidden;
    background: var(--page);
  }
  .canvas { position: relative; width: 1200px; height: 1051px; }
  .sign {
    position: absolute; left: 161px; top: 226px;
    width: 877px; height: 548px; overflow: hidden;
    background: radial-gradient(ellipse 70% 80% at 35% 45%, #ffffff 0%, #f4f4f4 55%, #e2e2e2 100%);
  }
  .sign__band {
    position: absolute; left: 0; right: 0; bottom: 0; height: 112px;
    background: linear-gradient(90deg, #ff2a2a 0%, #d40a0a 45%, #b00000 75%, #9a0000 100%);
  }
  .brand {
    position: absolute; left: 146px; top: 106px;
    display: flex; align-items: center; gap: 22px;
  }
  .brand__mark { width: 36px; height: 36px; background: var(--charcoal); }
  .brand__name {
    font-family: "Nunito", sans-serif; font-weight: 800;
    font-size: 104px; line-height: 1; letter-spacing: -2px;
    color: var(--maroon);
  }
  .tagline {
    position: absolute; left: 484px; top: 266px;
    font-family: "Nunito", sans-serif; font-weight: 700; line-height: 0.9;
  }
  .tagline__small { color: var(--grey-text); font-size: 31px; }
  .tagline__line { display: block; }
  .tagline__strong { font-size: 45px; font-weight: 800; letter-spacing: 1px; }
  .tagline__strong--maroon { color: var(--deep-red); }
  .tagline__strong--red { color: var(--brand-red); }
  .contact {
    position: absolute; left: 282px; top: 458px;
    font-family: "Nunito", sans-serif; color: var(--white);
  }
  .contact__phone { font-size: 45px; font-weight: 800; line-height: 1; letter-spacing: 1.5px; }
  .contact__web { font-size: 20.5px; font-weight: 700; line-height: 1; margin-top: 2px; margin-left: 2px; }
</style>
</head>
<body>
<main class="canvas">
  <section class="sign">
    <div class="sign__band" role="img" aria-label="Red faceted mountain graphic in layered red tones"></div>

    <div class="brand">
      <span class="brand__mark"></span>
      <span class="brand__name">bright path</span>
    </div>

    <p class="tagline">
      <span class="tagline__small tagline__line">Linking</span>
      <span class="tagline__strong tagline__strong--maroon tagline__line">Job Seekers</span>
      <span class="tagline__line"><span class="tagline__small">with </span><span class="tagline__strong tagline__strong--red">Employers</span></span>
    </p>

    <div class="contact">
      <p class="contact__phone">1300 482 917</p>
      <p class="contact__web">www.brightpathstaffing.com.au</p>
    </div>
  </section>
</main>
</body>
</html>
```